Postcard Design

www.lirvo.com.au
i am an occupational therapist and professionally trained coach. i work with children, parents and disability service providers to achieve brilliant outcomes for children with special needs.
http://www.lirvo.com.au/service/for-families
I need a postcard to give parents to promote our family service coaching service
A family service coach will work with you to set specific goals for your child, build a dream team, design and manage your child's highly effective therapy and educational team to ensure brilliant outcomes for your child..
KORLU - you have done my business card previously. they were great thank you.

```html
<!DOCTYPE html>
<html lang="en">
<head>
<meta charset="utf-8">
<title>Lirvo Family Service Coaching Postcard – Back</title>
<link rel="stylesheet" href="https://fonts.googleapis.com/css2?family=Arimo:wght@400;700&family=Questrial&display=swap">
<style>
  :root {
    --page-bg: #e6e7ea;
    --card-bg: #ffffff;
    --brand-blue: #2a58a3;
    --brand-blue-deep: #1f4a92;
    --brand-blue-light: #5b82bf;
    --text-blue: #2b4f95;
    --white: #ffffff;
  }
  * { margin: 0; padding: 0; box-sizing: border-box; }
  html, body {
    width: 1200px;
    height: 900px;
    overflow: hidden;
    background: var(--page-bg);
  }
  .postcard {
    position: absolute;
    left: 50px;
    top: 25px;
    width: 1100px;
    height: 851px;
    background: var(--card-bg);
    box-shadow: 0 4px 18px rgba(0, 0, 0, 0.12);
  }
  .banner {
    position: absolute;
    left: 0;
    top: 0;
    width: 827px;
    height: 273px;
    background: var(--brand-blue);
    overflow: hidden;
  }
  .banner-photo {
    position: absolute;
    right: 0;
    top: 0;
    width: 520px;
    height: 273px;
    background:
      radial-gradient(ellipse at 62% 45%, var(--brand-blue-light) 0%, rgba(91,130,191,0.35) 40%, rgba(42,88,163,0) 75%),
      linear-gradient(90deg, var(--brand-blue) 0%, var(--brand-blue-deep) 100%);
  }
  .brand {
    position: absolute;
    left: 189px;
    top: 108px;
    display: flex;
    align-items: center;
    gap: 18px;
  }
  .brand-dot {
    width: 56px;
    height: 56px;
    border-radius: 50%;
    background: var(--white);
  }
  .brand-name {
    font-family: "Arimo", Arial, sans-serif;
    font-weight: 700;
    font-size: 46px;
    line-height: 1;
    color: var(--white);
    letter-spacing: 0.5px;
  }
  .brand-url {
    position: absolute;
    left: 194px;
    top: 190px;
    font-family: "Arimo", Arial, sans-serif;
    font-size: 25px;
    color: var(--white);
  }
  .service-pitch {
    position: absolute;
    left: 167px;
    top: 312px;
    width: 340px;
    text-align: center;
    font-family: "Questrial", "Century Gothic", sans-serif;
    font-size: 26px;
    line-height: 38px;
    color: var(--text-blue);
  }
</style>
</head>
<body>
  <main class="postcard">
    <section class="banner">
      <div class="banner-photo" role="img" aria-label="Photograph of several hands joining jigsaw puzzle pieces together, tinted blue"></div>
      <div class="brand">
        <span class="brand-dot"></span>
        <span class="brand-name">lirvo</span>
      </div>
      <p class="brand-url">www.lirvo.com.au</p>
    </section>
    <p class="service-pitch">
      A family service coach<br>
      will work with you to set<br>
      specific goals for your<br>
      child, build a dream team,<br>
      design &nbsp;and manage your<br>
      child's &nbsp;highly &nbsp;effective<br>
      therapy and educational<br>
      team to ensure brilliant<br>
      outcomes for your child..
    </p>
  </main>
</body>
</html>
```